Business Card Design

I'm a young beekeeper (22 years old) just starting out. I own and run 80 hives and would like to eventually build up to 1000. My aim is to run it in tandem with our family farm that is currently running sheep and beef. Unlike a number of honey companies on the East Coast (or the North Island, NZ) I am local and will expand onto the lease blocks that our family is also leasing. I want a simple plain logo/photo. The designer may wish to use one of the photos as a background outline or however they chose. The mountain is Moekaha and our farm borders one side of it.

Target Market(s)

From local land owners to wholesale honey buyers

Industry/Entity Type

Farm

Contact Information for Business Card

Moekaha Honey
Manager Owner Rewene Tolland
email moekahahoney@pelvanmail.co.nz
mobile 0219473061

Requirements
Must have
• The details submitted. The brand Moekaha Honey to be the main feature. The other details can be smaller.
Should not have
• Must not include a picture of a bee or hive. Use a modern font. Don't use koru but may incorporate poutama.

```html
<!DOCTYPE html>
<html lang="en">
<head>
<meta charset="utf-8">
<title>Moekaha Honey — Business Card</title>
<link rel="stylesheet" href="https://fonts.googleapis.com/css2?family=Montserrat:wght@600;800&family=Tinos&display=swap">
<style>
  :root {
    --backdrop: #4a4a4c;
    --card-gold: #e1ad2c;
    --card-edge: #c9951f;
    --brand-brown: #9a5a1c;
    --ink: #1f1608;
  }
  html, body {
    margin: 0;
    padding: 0;
    overflow: hidden;
  }
  body {
    width: 1200px;
    height: 772px;
    background: var(--backdrop);
    display: flex;
    align-items: center;
    justify-content: center;
  }
  .business-card {
    position: relative;
    width: 400px;
    height: 620px;
    background: var(--card-gold);
    border-radius: 16px;
    box-shadow: 0 2px 0 var(--card-edge), 0 14px 30px rgba(0, 0, 0, 0.35);
    text-align: center;
    color: var(--ink);
  }
  .brand-mark {
    position: absolute;
    top: 118px;
    left: 50%;
    width: 44px;
    height: 44px;
    margin-left: -22px;
    background: var(--brand-brown);
    opacity: 0.85;
  }
  .brand-name {
    position: absolute;
    top: 200px;
    left: 0;
    right: 0;
    margin: 0;
    font-family: "Montserrat", sans-serif;
    font-weight: 600;
    font-size: 52px;
    line-height: 1.02;
    letter-spacing: 0.5px;
    color: var(--brand-brown);
  }
  .contact {
    position: absolute;
    top: 448px;
    left: 0;
    right: 0;
  }
  .contact-name {
    margin: 0 0 6px;
    font-family: "Montserrat", sans-serif;
    font-weight: 800;
    font-size: 16px;
    letter-spacing: 0.3px;
  }
  .contact-line {
    margin: 0;
    font-family: "Tinos", serif;
    font-size: 12.5px;
    line-height: 1.3;
  }
</style>
</head>
<body>
  <article class="business-card">
    <span class="brand-mark" aria-hidden="true"></span>
    <h1 class="brand-name">Moekaha<br>Honey</h1>
    <section class="contact">
      <p class="contact-name">Rewene Tolland</p>
      <p class="contact-line">Moekaha Honey Manager Owner</p>
      <p class="contact-line">email moekahahoney@pelvanmail.co.nz</p>
      <p class="contact-line">mobile 0219473061</p>
    </section>
  </article>
</body>
</html>
```